Christmas Collection Candle Label Design

Looking to update our existing Christmas Candle Collection labels. Labels should reflect the overall feel of our brand- www.kelvabrite.ca
Want to include some color elements. Holiday colors added into design but more muted/ earthy tones not vibrant colors . Metallic elements and line art botanical illustration. Fonts should be more align to brand
Scents
Winter Lantern
Frost Berry
Amber and Fig
Belle Étoile

```html
<!DOCTYPE html>
<html lang="en">
<head>
<meta charset="utf-8">
<title>Kelvabrite Christmas Collection Labels</title>
<link rel="stylesheet" href="https://fonts.googleapis.com/css2?family=Cinzel:wght@500;600&family=EB+Garamond:wght@400;500&display=swap">
<style>
  :root {
    --paper: #ddd5c5;
    --ink: #3f4a33;
    --rule: #4a5340;
    --ring: #9a9386;
    --band-text: #ffffff;
    --green-hi: #b9d3a6; --green-mid: #5e9440; --green-lo: #245a0c;
    --red-hi: #f6a3a3; --red-mid: #d4343c; --red-lo: #9c1e26;
    --silver-hi: #f4f4f4; --silver-mid: #c8c8ca; --silver-lo: #858587;
    --gold-hi: #f8f0a8; --gold-mid: #d8b55a; --gold-lo: #a87a1c;
  }
  * { margin: 0; padding: 0; box-sizing: border-box; }
  html, body { width: 1176px; height: 1200px; overflow: hidden; background: #ffffff; }
  .sheet { position: relative; width: 1176px; height: 1200px; }

  .label {
    position: absolute; width: 458px; height: 561px;
    background: var(--paper);
    border-radius: 0 37px 20px 20px;
    overflow: hidden;
    font-family: "EB Garamond", Georgia, serif;
    color: var(--ink);
  }
  .label--winter { left: 0; top: 2px; --hi: var(--green-hi); --mid: var(--green-mid); --lo: var(--green-lo); --art: #c6d2b4; }
  .label--frost  { left: 717px; top: 0; border-radius: 37px 37px 20px 20px; --hi: var(--red-hi); --mid: var(--red-mid); --lo: var(--red-lo); --art: #e2b8b4; }
  .label--amber  { left: 0; top: 638px; --hi: var(--silver-hi); --mid: var(--silver-mid); --lo: var(--silver-lo); --art: #c9c6cc; }
  .label--belle  { left: 715px; top: 637px; border-radius: 37px 37px 20px 20px; --hi: var(--gold-hi); --mid: var(--gold-mid); --lo: var(--gold-lo); --art: #e2d2a8; }

  .tagline {
    position: absolute; left: 41px; top: 69px;
    font-size: 15.5px; font-weight: 500; letter-spacing: 1.8px;
  }
  .rule { position: absolute; left: 42px; height: 2.5px; background: var(--rule); }
  .rule--top { top: 133px; width: 290px; }
  .rule--bottom { top: 321px; width: 201px; }

  .title {
    position: absolute; left: 40px; top: 165px;
    font-family: "Cinzel", "Times New Roman", serif;
    font-weight: 600; font-size: 52px; line-height: 64px;
    letter-spacing: 1px; text-transform: uppercase;
    background: linear-gradient(180deg, var(--hi) 0%, var(--mid) 55%, var(--lo) 100%);
    background-size: 100% 64px;
    -webkit-background-clip: text; background-clip: text;
    color: transparent;
  }
  .title .amp { font-size: 38px; }

  .notes {
    position: absolute; left: 41px; top: 350px;
    font-size: 16px; font-weight: 500; letter-spacing: 1.6px;
  }

  .seal { position: absolute; left: 246px; top: 283px; width: 196px; height: 196px; }
  .seal__ring { fill: none; stroke: var(--ring); stroke-width: 1; opacity: .7; }
  .seal__art { fill: var(--art); opacity: .6; }

  .band {
    position: absolute; left: 0; right: 0; bottom: 0; height: 49px;
    background: linear-gradient(180deg, var(--mid) 0%, var(--hi) 30%, var(--mid) 65%, var(--lo) 100%);
    display: flex; align-items: center;
    color: var(--band-text); font-size: 13px; letter-spacing: 1.4px;
  }
  .band__cell { height: 32px; display: flex; align-items: center; justify-content: center; }
  .band__cell--weight { width: 152px; font-size: 12.5px; letter-spacing: .3px; }
  .band__cell--origin { width: 153px; border-left: 1.5px solid var(--band-text); border-right: 1.5px solid var(--band-text); }
  .band__cell--line { flex: 1; }
</style>
</head>
<body>
<main class="sheet">

  <article class="label label--winter">
    <p class="tagline">made with plant based botanicals</p>
    <div class="rule rule--top"></div>
    <h1 class="title">Winter<br>Lantern</h1>
    <div class="rule rule--bottom"></div>
    <p class="notes">pine secent - oak - clove</p>
    <svg class="seal" viewBox="0 0 196 196">
      <circle class="seal__ring" cx="98" cy="98" r="95"/>
      <ellipse class="seal__art" cx="98" cy="98" rx="58" ry="70" role="img" aria-label="Line art pine sprig illustration"/>
    </svg>
    <footer class="band">
      <span class="band__cell band__cell--weight">Net Wt. 10 Oz/253 g</span>
      <span class="band__cell band__cell--origin">Made in Canada</span>
      <span class="band__cell band__cell--line">Kelva Soy</span>
    </footer>
  </article>

  <article class="label label--frost">
    <p class="tagline">made with plant based botanicals</p>
    <div class="rule rule--top"></div>
    <h1 class="title">Frost<br>Berry</h1>
    <div class="rule rule--bottom"></div>
    <p class="notes">candy secent - peppermint</p>
    <svg class="seal" viewBox="0 0 196 196">
      <circle class="seal__ring" cx="98" cy="98" r="95"/>
      <ellipse class="seal__art" cx="98" cy="98" rx="50" ry="72" role="img" aria-label="Line art peppermint sticks illustration"/>
    </svg>
    <footer class="band">
      <span class="band__cell band__cell--weight">Net Wt. 10 Oz/253 g</span>
      <span class="band__cell band__cell--origin">Made in Canada</span>
      <span class="band__cell band__cell--line">Kelva Soy</span>
    </footer>
  </article>

  <article class="label label--amber">
    <p class="tagline">made with plant based botanicals</p>
    <div class="rule rule--top"></div>
    <h1 class="title">Amber <span class="amp">&amp;</span><br>Fig</h1>
    <div class="rule rule--bottom"></div>
    <p class="notes">pine secent - oak - clove</p>
    <svg class="seal" viewBox="0 0 196 196">
      <circle class="seal__ring" cx="98" cy="98" r="95"/>
      <ellipse class="seal__art" cx="98" cy="98" rx="52" ry="62" role="img" aria-label="Line art snowflakes illustration"/>
    </svg>
    <footer class="band">
      <span class="band__cell band__cell--weight">Net Wt. 10 Oz/253 g</span>
      <span class="band__cell band__cell--origin">Made in Canada</span>
      <span class="band__cell band__cell--line">Kelva Soy</span>
    </footer>
  </article>

  <article class="label label--belle">
    <p class="tagline">made with plant based botanicals</p>
    <div class="rule rule--top"></div>
    <h1 class="title">Belle<br>Étoile</h1>
    <div class="rule rule--bottom"></div>
    <p class="notes">pine secent - oak - clove</p>
    <svg class="seal" viewBox="0 0 196 196">
      <circle class="seal__ring" cx="98" cy="98" r="95"/>
      <ellipse class="seal__art" cx="98" cy="98" rx="58" ry="68" role="img" aria-label="Line art pine cones illustration"/>
    </svg>
    <footer class="band">
      <span class="band__cell band__cell--weight">Net Wt. 10 Oz/253 g</span>
      <span class="band__cell band__cell--origin">Made in Canada</span>
      <span class="band__cell band__cell--line">Kelva Soy</span>
    </footer>
  </article>

</main>
</body>
</html>
```